QORLIN Business card. A.I. company developing trading strategies.

My name is marcello bianchi and I'm CEO and co-founder of QORLIN Research, an AI company focusing on generating Ai-driven trading strategies.
This is our website: https://qorlin-analytics.example/
Values of our company: tech & R&D driven (we're all very mathy/stats/data driven), sophisticated (we only look for sophisticated, high knowledge investors), reserved (we don't go around telling anyone what we do).
Our main product: PivotFund. A trading strategy that delivered 70% in 2022 and 20% in 2023 so far.
Our main potential clients: HNW individuals, hedge funds, asset managers, tech entrepreneur.
Target Market(s)
Hedge funds, asset managers, High Net Worth individuals, Pension funds
Contact Information for Business Card
The basic: name, job title, company name, address, mail, phone number

```html
<!DOCTYPE html>
<html lang="en">
<head>
<meta charset="utf-8">
<title>QORLIN Research – Business Card</title>
<link href="https://fonts.googleapis.com/css2?family=Raleway:wght@300;400;600;800&display=swap" rel="stylesheet">
<style>
  :root {
    --backdrop: #d0d0d0;
    --card-dark-start: #131416;
    --card-dark-end: #282b31;
    --card-light: #ffffff;
    --decor-dark: rgba(92, 93, 96, 0.28);
    --decor-light: rgba(212, 213, 215, 0.45);
    --accent-red: #a3283a;
    --ink: #2a2a2e;
    --ink-soft: #6a6a70;
    --white: #ffffff;
  }
  * { box-sizing: border-box; margin: 0; padding: 0; }
  html, body {
    width: 1200px; height: 1000px; overflow: hidden;
    background: var(--backdrop);
    font-family: "Raleway", sans-serif;
  }
  .card {
    position: absolute;
    left: 293px;
    width: 614px; height: 353px;
    overflow: hidden;
  }
  .card--front {
    top: 118px;
    background: linear-gradient(90deg, var(--card-dark-start) 0%, var(--card-dark-end) 60%, #25282d 100%);
  }
  .card--back {
    top: 525px;
    background: var(--card-light);
  }
  .card__decor {
    position: absolute; left: 0; top: 0;
    width: 260px; height: 353px;
  }
  .card--front .card__decor {
    background: linear-gradient(90deg, var(--decor-dark) 0%, transparent 100%);
  }
  .card--back .card__decor {
    background: linear-gradient(90deg, var(--decor-light) 0%, transparent 100%);
  }
  .wordmark {
    position: absolute;
    display: flex; align-items: center; gap: 6px;
    font-weight: 300;
    font-size: 40px;
    letter-spacing: 3px;
    line-height: 1;
  }
  .wordmark__dot {
    width: 8px; height: 8px; border-radius: 50%;
    background: var(--accent-red);
  }
  .card--front .wordmark {
    left: 312px; top: 156px;
    color: var(--white);
  }
  .card--back .wordmark {
    right: 50px; top: 36px;
    color: var(--ink);
  }
  .contact {
    position: absolute;
    right: 50px; top: 145px;
    text-align: right;
    color: var(--ink);
  }
  .contact__name {
    font-weight: 800;
    font-size: 28px;
    color: var(--accent-red);
    line-height: 1.1;
  }
  .contact__role {
    margin-top: 8px;
    font-size: 11px;
    letter-spacing: 1.2px;
    color: var(--ink-soft);
    text-transform: uppercase;
  }
  .contact__company {
    margin-top: 20px;
    font-weight: 600;
    font-size: 18px;
    line-height: 22px;
  }
  .contact__line {
    font-weight: 300;
    font-size: 18px;
    line-height: 22px;
  }
</style>
</head>
<body>

  <section class="card card--front" aria-label="Business card front">
    <div class="card__decor" role="img" aria-label="Decorative area in soft grey tones"></div>
    <div class="wordmark">QORLIN<span class="wordmark__dot"></span></div>
  </section>

  <section class="card card--back" aria-label="Business card back">
    <div class="card__decor" role="img" aria-label="Decorative area in light grey tones"></div>
    <div class="wordmark">QORLIN<span class="wordmark__dot"></span></div>
    <div class="contact">
      <p class="contact__name">Marcello Bianchi</p>
      <p class="contact__role">CEO and Co-Founder</p>
      <p class="contact__company">QORLIN Research</p>
      <p class="contact__line">14 rue des Lilas Bleus 75011 Paris</p>
      <p class="contact__line">office@qorlin-analytics.example</p>
      <p class="contact__line">604318275</p>
    </div>
  </section>

</body>
</html>
```